Verostel business card

Business card for sustainable investment company called "Verostel". Verostel is an exchange platform selling carbon credits between buyers and sellers. Carbon Credits are an environmental commodity for reducing global carbon emissions.

the card should obviously have our logo and the theme should be sustainability/environment mixed with a trading platform.

Contact Information for Business Card

Logo, Name, Title, Phone, Email

Colors
0054AA
0677BA
7BADD7
CADEEF
E8F1F8
0094D4
00A9DD
6FCCEA
C7EBF8
E9F6FB
00AB8E
00BBA5
67D7C9
C6EFE9
E9F9F6
59FF00
82FF00
B8FF75
E3FFCB
F4FFEA

```html
<!DOCTYPE html>
<html lang="en">
<head>
<meta charset="utf-8">
<title>Verostel Business Card</title>
<link href="https://fonts.googleapis.com/css2?family=Montserrat:wght@400;500;600;700&display=swap" rel="stylesheet">
<style>
  :root {
    --stage: #e6e8ec;
    --navy-deep: #101f45;
    --navy: #152a5a;
    --navy-light: #1b3468;
    --accent: #4fb3e2;
    --accent-soft: #6fcbea;
    --rule: #3f86b8;
    --white: #ffffff;
  }
  * { margin: 0; padding: 0; box-sizing: border-box; }
  html, body {
    width: 1200px;
    height: 900px;
    overflow: hidden;
    background: var(--stage);
    font-family: "Montserrat", sans-serif;
  }
  .stage {
    position: relative;
    width: 1200px;
    height: 900px;
  }
  .card {
    position: absolute;
    left: 280px;
    width: 640px;
    height: 366px;
    border-radius: 0 44px 0 44px;
    overflow: hidden;
    box-shadow: 0 10px 24px rgba(16, 31, 69, 0.22);
  }
  .card-back {
    top: 64px;
    background: var(--navy);
  }
  .back-pattern {
    position: absolute;
    inset: 0;
    background: linear-gradient(135deg, var(--navy-light) 0%, var(--navy) 55%, var(--navy-deep) 100%);
  }
  .back-brand {
    position: absolute;
    right: 42px;
    top: 150px;
    display: flex;
    align-items: center;
    gap: 8px;
  }
  .brand-square {
    display: block;
    background: var(--accent);
  }
  .back-brand .brand-square { width: 14px; height: 14px; }
  .back-brand .brand-name {
    color: var(--white);
    font-weight: 600;
    font-size: 18px;
    letter-spacing: 0.04em;
  }
  .card-front {
    top: 470px;
    background: linear-gradient(90deg, var(--navy) 0%, var(--navy-light) 70%, var(--navy) 100%);
  }
  .contact {
    position: absolute;
    right: 54px;
    top: 50px;
    text-align: right;
  }
  .person-name {
    color: var(--accent);
    font-weight: 500;
    font-size: 17px;
    letter-spacing: 0.06em;
    text-transform: uppercase;
  }
  .person-title {
    color: var(--white);
    font-size: 15px;
    margin-top: 2px;
  }
  .contact-list {
    list-style: none;
    margin-top: 30px;
  }
  .contact-list li {
    display: flex;
    justify-content: flex-end;
    align-items: center;
    gap: 8px;
    color: var(--white);
    font-size: 17px;
    line-height: 30px;
  }
  .contact-list svg { width: 14px; height: 14px; }
  .divider {
    position: absolute;
    left: 230px;
    right: 48px;
    top: 236px;
    height: 1px;
    background: var(--rule);
  }
  .front-brand {
    position: absolute;
    right: 50px;
    bottom: 52px;
    display: flex;
    align-items: center;
    gap: 16px;
  }
  .front-brand .brand-square { width: 34px; height: 34px; }
  .front-brand .brand-name {
    color: var(--white);
    font-weight: 600;
    font-size: 50px;
    letter-spacing: 0.02em;
    line-height: 1;
    text-transform: uppercase;
  }
</style>
</head>
<body>
<main class="stage">
  <section class="card card-back">
    <div class="back-pattern" role="img" aria-label="Tonal pattern of repeated brand marks across the card back"></div>
    <div class="back-brand">
      <span class="brand-square"></span>
      <span class="brand-name">Verostel</span>
    </div>
  </section>

  <section class="card card-front">
    <div class="contact">
      <p class="person-name">Daniel Hart</p>
      <p class="person-title">Director</p>
      <ul class="contact-list">
        <li>415-382-7160
          <svg viewBox="0 0 24 24" aria-hidden="true"><path fill="#4fb3e2" d="M6.6 10.8a15 15 0 0 0 6.6 6.6l2.2-2.2a1 1 0 0 1 1-.25 11.4 11.4 0 0 0 3.6.57 1 1 0 0 1 1 1V20a1 1 0 0 1-1 1A17 17 0 0 1 3 4a1 1 0 0 1 1-1h3.5a1 1 0 0 1 1 1c0 1.25.2 2.45.57 3.57a1 1 0 0 1-.25 1z"/></svg>
        </li>
        <li>info@verostel.com
          <svg viewBox="0 0 24 24" aria-hidden="true"><path fill="#4fb3e2" d="M3 5h18a1 1 0 0 1 1 1v12a1 1 0 0 1-1 1H3a1 1 0 0 1-1-1V6a1 1 0 0 1 1-1zm1 2.2V17h16V7.2l-8 5.3z"/></svg>
        </li>
      </ul>
    </div>
    <div class="divider"></div>
    <div class="front-brand">
      <span class="brand-square"></span>
      <span class="brand-name">Verostel</span>
    </div>
  </section>
</main>
</body>
</html>
```